Quillon’s Prime Response Vehicle Branding

I am looking to get a half wrap for vehicles to assist in branding for a fire water storm and mold restoration company. I would like to have something similar to the photo loaded to include RWTB Certified Firm Logo and we also use Vans and Trucks...

Target Market(s)

Insurance claims damage from fire water floods and storms and mold....

Requirements
Must have
• The listed logo that I have uploaded. I would also like to have the fact of services provided (see below of services provided)
I would like something for the back of trucks / vans also to be included.

Please list where it looks uniform the following:
- Property Damage Restoration Specialist.
- 24 hr Emergency Service
- Web site: Quillonprimeresponse.com
- Office line: 904-618-3927

Services Provided to list:
Fire - Water - Mold - Storm
Restoration
Nice to have
• I would like to have some designs that incorporate in the background showing fire, wind / water / possibly if that can fit into what you design and it does not need to overwhelm the design though...
Should not have
• I do not want the logo changed.
I do not want it to be to busy.

```html
<!DOCTYPE html>
<html lang="en">
<head>
<meta charset="utf-8">
<title>Quillon’s Prime Response – Vehicle Wrap Concepts</title>
<link rel="stylesheet" href="https://fonts.googleapis.com/css2?family=Oswald:wght@500;600&display=swap">
<style>
  :root {
    --stage: #6d6e71;
    --body: #ffffff;
    --body-line: #a7a9ac;
    --glass: #123b45;
    --tyre: #231f20;
    --trim: #d1d3d4;
    --brand-red: #b5121b;
    --ink: #111111;
    --paper: #ffffff;
  }
  html, body { margin: 0; padding: 0; overflow: hidden; background: var(--stage); }
  .sheet { width: 1200px; height: 752px; display: block; }
  .label { font: 600 34px 'Oswald', sans-serif; fill: var(--ink); }
  .wrap-text { font-family: 'Oswald', sans-serif; font-weight: 500; }
  .headline { fill: var(--paper); }
  .brand-name { fill: var(--ink); }
  .phone { fill: var(--brand-red); }
  .web { fill: var(--ink); }
  .web-red { fill: var(--brand-red); }
  .service { fill: var(--ink); }
  .service-light { fill: var(--paper); }
  .service-tag { fill: var(--brand-red); }
  .body-shell { fill: var(--body); stroke: var(--body-line); stroke-width: 3; }
  .glass { fill: var(--glass); }
  .tyre { fill: var(--tyre); }
  .rim { fill: none; stroke: #bcbec0; stroke-width: 6; }
  .arch { fill: #2b2b2b; }
  .trim { fill: var(--trim); stroke: var(--body-line); stroke-width: 2; }
  .icon-dark { fill: none; stroke: var(--ink); stroke-width: 3; }
  .icon-light { fill: none; stroke: var(--paper); stroke-width: 2.5; }
  .badge { fill: var(--paper); stroke: #444; stroke-width: 2; }
  .shadow { fill: #5b5c5f; }
</style>
</head>
<body>
<svg class="sheet" viewBox="0 0 2415 1512" xmlns="http://www.w3.org/2000/svg">
  <defs>
    <linearGradient id="bed-red" x1="0" x2="1" y1="0" y2="0">
      <stop offset="0" stop-color="#c4161c"/>
      <stop offset="0.55" stop-color="#7a0d12"/>
      <stop offset="1" stop-color="#111"/>
    </linearGradient>
    <linearGradient id="storm-fire" x1="0" x2="1" y1="0" y2="1">
      <stop offset="0" stop-color="#5a4fb0"/>
      <stop offset="0.45" stop-color="#1f3f73"/>
      <stop offset="0.8" stop-color="#f26522"/>
      <stop offset="1" stop-color="#ffb000"/>
    </linearGradient>
    <linearGradient id="fire-storm-diag" x1="0" x2="1" y1="1" y2="0">
      <stop offset="0" stop-color="#ff8a00"/>
      <stop offset="0.35" stop-color="#d9480f"/>
      <stop offset="0.6" stop-color="#1f3f73"/>
      <stop offset="1" stop-color="#6a5fc1"/>
    </linearGradient>
  </defs>

  <text class="label" x="314" y="287">Design A</text>

  <g class="truck truck-side-a">
    <ellipse class="shadow" cx="870" cy="688" rx="680" ry="16"/>
    <path class="body-shell" role="img" aria-label="Pickup truck, side view" d="M215,370 L668,378 L670,262 Q680,252 720,252 L1060,262 L1230,372 L1490,392 L1515,440 L1522,560 L1430,590 L250,590 L195,575 L195,520 L218,500 Z"/>
    <rect class="glass" x="710" y="275" width="178" height="103"/>
    <path class="glass" d="M928,275 L1060,278 L1160,360 L1150,385 L928,385 Z"/>

    <g class="wrap wrap-side-a">
      <path fill="url(#bed-red)" d="M217,372 L668,378 L668,588 L250,588 L217,560 Z"/>
      <path fill="url(#storm-fire)" role="img" aria-label="Storm lightning, water and fire imagery in stacked frames" d="M590,380 L808,400 L770,585 L580,585 Z"/>
      <text class="wrap-text headline" x="462" y="402" font-size="24" text-anchor="middle">Property Damage</text>
      <text class="wrap-text headline" x="462" y="424" font-size="24" text-anchor="middle">Restoration Experts</text>
      <text class="wrap-text headline" x="322" y="430" font-size="22" text-anchor="middle">24/7 Service</text>
      <rect class="badge" x="293" y="450" width="36" height="52" rx="3"/>

      <g class="service-list">
        <path class="icon-dark" d="M835,422 C822,436 822,452 835,454 C848,452 848,436 835,422 Z"/>
        <text class="wrap-text service" x="862" y="452" font-size="26">Fire</text>
        <path class="icon-dark" d="M833,462 C826,472 826,482 833,484 C840,482 840,472 833,462 Z"/>
        <text class="wrap-text service" x="862" y="488" font-size="26">Water</text>
        <path class="icon-dark" d="M822,500 H848 M826,508 H844 M830,516 H840 M834,524 H838"/>
        <text class="wrap-text service" x="862" y="520" font-size="26">Storm</text>
        <circle class="icon-dark" cx="833" cy="547" r="6"/>
        <circle class="icon-dark" cx="820" cy="540" r="3"/>
        <circle class="icon-dark" cx="846" cy="540" r="3"/>
        <circle class="icon-dark" cx="822" cy="558" r="3"/>
        <circle class="icon-dark" cx="845" cy="558" r="3"/>
        <text class="wrap-text service" x="862" y="557" font-size="26">Mold</text>
      </g>

      <g class="brand-block">
        <rect x="925" y="430" width="40" height="40" fill="var(--brand-red)"/>
        <text class="wrap-text brand-name" x="975" y="458" font-size="30">Quillon’s Prime</text>
        <text class="wrap-text brand-name" x="975" y="492" font-size="30">Response</text>
        <text class="wrap-text phone" x="1040" y="537" font-size="40" text-anchor="middle">904-618-3927</text>
        <text class="wrap-text web" x="1042" y="557" font-size="17" text-anchor="middle">quillonprimeresponse.com</text>
      </g>
    </g>

    <path class="arch" d="M340,590 Q360,445 462,445 Q565,445 585,590 Z"/>
    <path class="arch" d="M1190,590 Q1210,450 1312,450 Q1415,450 1435,590 Z"/>
    <circle class="tyre" cx="462" cy="592" r="100"/>
    <circle class="rim" cx="462" cy="592" r="58"/>
    <circle class="tyre" cx="1312" cy="592" r="100"/>
    <circle class="rim" cx="1312" cy="592" r="58"/>
    <rect class="trim" x="195" y="520" width="60" height="56" rx="6"/>
  </g>

  <g class="truck truck-front">
    <ellipse class="shadow" cx="1918" cy="688" rx="300" ry="14"/>
    <path class="body-shell" role="img" aria-label="Pickup truck, front view" d="M1780,258 L2060,258 L2120,365 L2150,420 L2150,600 L1690,600 L1690,420 L1720,365 Z"/>
    <path class="glass" d="M1790,272 L2050,272 L2100,365 L1735,365 Z"/>
    <rect x="1795" y="412" width="250" height="85" fill="#2b2b2b" rx="4"/>
    <circle cx="1742" cy="440" r="16" fill="#8fd3f4" stroke="#333" stroke-width="4"/>
    <circle cx="2095" cy="440" r="16" fill="#8fd3f4" stroke="#333" stroke-width="4"/>
    <rect class="trim" x="1790" y="555" width="250" height="40"/>
    <rect class="tyre" x="1685" y="600" width="60" height="90" rx="8"/>
    <rect class="tyre" x="2092" y="600" width="60" height="90" rx="8"/>
    <rect class="trim" x="1660" y="338" width="60" height="32" rx="6"/>
    <rect class="trim" x="2118" y="338" width="60" height="32" rx="6"/>
  </g>

  <text class="label" x="314" y="977">Design B</text>

  <g class="truck truck-side-b">
    <ellipse class="shadow" cx="910" cy="1343" rx="680" ry="16"/>
    <path class="body-shell" role="img" aria-label="Pickup truck, side view" d="M1558,1025 L1110,1030 L1108,918 Q1095,908 1060,910 L700,915 L540,1030 L300,1048 L265,1090 L252,1225 L345,1245 L1500,1245 L1580,1230 L1580,1180 L1555,1160 Z"/>
    <path class="glass" d="M660,932 L845,932 L835,1035 L610,1038 Z"/>
    <path class="glass" d="M888,930 L1062,930 L1065,1030 L888,1035 Z"/>

    <g class="wrap wrap-side-b">
      <path fill="var(--ink)" d="M650,1242 L1112,1012 L1462,1030 L1370,1242 Z"/>
      <path fill="url(#fire-storm-diag)" role="img" aria-label="Fire, water and lightning storm imagery along the diagonal" d="M660,1242 L1112,1020 L1112,1085 L900,1242 Z"/>
      <path fill="var(--brand-red)" d="M640,1242 L1112,1004 L1112,1020 L662,1242 Z"/>
      <path fill="var(--brand-red)" d="M1418,1030 L1462,1030 L1398,1098 L1362,1098 Z"/>
      <text class="wrap-text headline" x="1270" y="1062" font-size="24" text-anchor="middle">Property Damage</text>
      <text class="wrap-text headline" x="1270" y="1084" font-size="24" text-anchor="middle">Restoration Experts</text>
      <text class="wrap-text service-tag" x="1158" y="1140" font-size="22" text-anchor="middle">24/7 Service</text>
      <rect class="badge" x="1128" y="1170" width="34" height="50" rx="3"/>

      <g class="service-row">
        <path class="icon-light" d="M958,1183 C948,1194 948,1206 958,1208 C968,1206 968,1194 958,1183 Z"/>
        <text class="wrap-text service-light" x="958" y="1226" font-size="15" text-anchor="middle">Fire</text>
        <path class="icon-light" d="M994,1186 C987,1196 987,1204 994,1206 C1001,1204 1001,1196 994,1186 Z"/>
        <text class="wrap-text service-light" x="994" y="1226" font-size="15" text-anchor="middle">Water</text>
        <path class="icon-light" d="M1024,1188 H1048 M1028,1195 H1044 M1032,1202 H1040"/>
        <text class="wrap-text service-light" x="1036" y="1226" font-size="15" text-anchor="middle">Storm</text>
        <circle class="icon-light" cx="1077" cy="1197" r="5"/>
        <circle class="icon-light" cx="1066" cy="1189" r="2.5"/>
        <circle class="icon-light" cx="1088" cy="1189" r="2.5"/>
        <circle class="icon-light" cx="1068" cy="1206" r="2.5"/>
        <circle class="icon-light" cx="1087" cy="1206" r="2.5"/>
        <text class="wrap-text service-light" x="1077" y="1226" font-size="15" text-anchor="middle">Mold</text>
      </g>

      <g class="brand-block">
        <rect x="606" y="1082" width="46" height="46" fill="var(--brand-red)"/>
        <text class="wrap-text brand-name" x="664" y="1104" font-size="30">Quillon’s Prime</text>
        <text class="wrap-text brand-name" x="664" y="1136" font-size="30">Response</text>
        <text class="wrap-text phone" x="604" y="1166" font-size="31">904-618-3927</text>
      </g>
      <text class="wrap-text web-red" x="470" y="1084" font-size="20" text-anchor="middle" transform="rotate(-2 470 1084)">quillonprimeresponse.com</text>
    </g>

    <path class="arch" d="M340,1248 Q360,1105 462,1105 Q565,1105 585,1248 Z"/>
    <path class="arch" d="M1190,1248 Q1210,1100 1312,1100 Q1415,1100 1435,1248 Z"/>
    <circle class="tyre" cx="462" cy="1250" r="100"/>
    <circle class="rim" cx="462" cy="1250" r="58"/>
    <circle class="tyre" cx="1312" cy="1250" r="100"/>
    <circle class="rim" cx="1312" cy="1250" r="58"/>
    <rect class="trim" x="1520" y="1178" width="62" height="55" rx="6"/>
    <rect x="1508" y="1055" width="46" height="85" fill="var(--brand-red)" rx="4"/>
  </g>

  <g class="truck truck-rear">
    <ellipse class="shadow" cx="1918" cy="1343" rx="300" ry="14"/>
    <path class="body-shell" role="img" aria-label="Pickup truck, rear view" d="M1790,905 L2050,905 L2100,1020 L2145,1045 L2145,1250 L1690,1250 L1690,1045 L1735,1020 Z"/>
    <path class="glass" d="M1795,920 L2045,920 L2100,1020 L1735,1020 Z"/>
    <rect x="1697" y="1050" width="38" height="92" fill="var(--brand-red)" rx="4"/>
    <rect x="2105" y="1050" width="38" height="92" fill="var(--brand-red)" rx="4"/>

    <g class="wrap wrap-rear">
      <rect x="1735" y="1030" width="370" height="140" fill="var(--paper)"/>
      <path fill="var(--ink)" d="M2050,1030 L2105,1030 L2105,1170 L1800,1170 Z"/>
      <path fill="url(#fire-storm-diag)" role="img" aria-label="Fire and lightning storm imagery along the diagonal" d="M1745,1168 L1998,1030 L2050,1030 L1800,1170 Z"/>
      <path fill="var(--brand-red)" d="M1735,1162 L1990,1030 L1998,1030 L1745,1170 L1735,1170 Z"/>
      <path fill="var(--brand-red)" d="M2090,1125 L2105,1118 L2105,1150 L2075,1165 Z"/>

      <rect x="1745" y="1058" width="20" height="26" fill="var(--brand-red)"/>
      <text class="wrap-text brand-name" x="1772" y="1071" font-size="14">Quillon’s Prime</text>
      <text class="wrap-text brand-name" x="1772" y="1087" font-size="14">Response</text>
      <text class="wrap-text phone" x="1742" y="1107" font-size="15">904-618-3927</text>
      <rect class="badge" x="1743" y="1120" width="14" height="18" rx="2"/>

      <text class="wrap-text service-tag" x="2060" y="1074" font-size="14" text-anchor="middle">24/7 Service</text>
      <g class="service-row">
        <path class="icon-light" d="M1985,1083 C1979,1090 1979,1098 1985,1099 C1991,1098 1991,1090 1985,1083 Z"/>
        <text class="wrap-text service-light" x="1985" y="1114" font-size="10" text-anchor="middle">Fire</text>
        <path class="icon-light" d="M2012,1086 C2008,1092 2008,1097 2012,1098 C2016,1097 2016,1092 2012,1086 Z"/>
        <text class="wrap-text service-light" x="2012" y="1114" font-size="10" text-anchor="middle">Water</text>
        <path class="icon-light" d="M2036,1088 H2052 M2039,1093 H2049 M2042,1098 H2046"/>
        <text class="wrap-text service-light" x="2044" y="1114" font-size="10" text-anchor="middle">Storm</text>
        <circle class="icon-light" cx="2076" cy="1093" r="3"/>
        <text class="wrap-text service-light" x="2076" y="1114" font-size="10" text-anchor="middle">Mold</text>
      </g>
      <text class="wrap-text headline" x="1973" y="1139" font-size="18" text-anchor="middle">Property Damage</text>
      <text class="wrap-text headline" x="1973" y="1157" font-size="18" text-anchor="middle">Restoration Experts</text>
    </g>

    <rect class="trim" x="1690" y="1178" width="455" height="40"/>
    <rect x="1885" y="1180" width="70" height="32" fill="var(--paper)"/>
    <rect class="tyre" x="1690" y="1250" width="60" height="95" rx="8"/>
    <rect class="tyre" x="2087" y="1250" width="60" height="95" rx="8"/>
    <rect class="trim" x="1668" y="985" width="55" height="30" rx="6"/>
    <rect class="trim" x="2115" y="985" width="55" height="30" rx="6"/>
  </g>
</svg>
</body>
</html>
```